Painted Lanterns- Ever think you'd get a second chance. Ever think you'd get two...

The story is about a woman, mid-40's who gave up on her dreams and her love because of jealousy. Now, 20 years later, she is now a restaurant owner in her little town, but never stops thinking about what she gave up. When a movie project comes to town, she is given a second chance at both. Will she take them?

Target Market(s)

Women 35 to 60

Industry/Entity Type

Entertainment Industry

Font styles to use
Serif
Script

Requirements
Must have
• Deeply feminine...But not overly patronizing.
Nice to have
• Flowery feel.
Should not have
• Dark colors. Sadness.

```html
<!DOCTYPE html>
<html lang="en">
<head>
<meta charset="utf-8">
<title>Painted Lanterns – Poster</title>
<link rel="stylesheet" href="https://fonts.googleapis.com/css2?family=Montserrat:wght@300;400;600;700;800&family=Cinzel:wght@400;600&display=swap">
<style>
  :root {
    --magenta: #c2197b;
    --ink: #2a2a2a;
    --paper: #ffffff;
    --backdrop: #e9e7e8;
    --frame: #ffffff;
  }
  * { box-sizing: border-box; margin: 0; padding: 0; }
  html, body { width: 1200px; height: 861px; overflow: hidden; background: var(--backdrop); }
  .stage { position: relative; width: 1200px; height: 861px; }
  .poster {
    position: absolute; left: 308px; top: 20px; width: 584px; height: 820px;
    background: var(--paper); overflow: hidden;
    box-shadow: 0 6px 18px rgba(0,0,0,.18);
    font-family: "Montserrat", sans-serif; color: var(--ink); text-align: center;
  }
  .key-photo {
    position: absolute; left: 0; top: 0; width: 584px; height: 362px;
    background:
      radial-gradient(ellipse at 78% 55%, rgba(80,70,110,.55), transparent 45%),
      linear-gradient(90deg, #7f9a7c 0%, #a9b8a6 30%, #d9dde0 45%, #ccd3da 55%, #4a6a8f 68%, #b9b3b8 85%, #c9a5aa 100%);
  }
  .accent-band {
    position: absolute; left: 0; top: 372px; width: 584px; height: 17px; background: var(--magenta);
  }
  .still {
    position: absolute; top: 305px; width: 133px; height: 131px;
    border: 7px solid var(--frame); background: var(--frame);
  }
  .still span { display: block; width: 100%; height: 100%; }
  .still--night { left: 57px; } .still--night span { background: linear-gradient(135deg, #3a3a38, #1c1c1e 60%, #4a4642); }
  .still--sepia { left: 225px; } .still--sepia span { background: linear-gradient(160deg, #8a7868, #5c4c40 60%, #9a8a7a); }
  .still--cafe { left: 391px; } .still--cafe span { background: linear-gradient(135deg, #d8e0e0, #7d8f8c 50%, #3d4a4a); }
  .studios {
    position: absolute; top: 443px; left: 0; width: 100%;
    font-weight: 700; font-size: 15px; color: var(--magenta); letter-spacing: .2px; white-space: nowrap;
  }
  .studios small, .association small { font-size: 8.5px; font-weight: 400; color: var(--ink); letter-spacing: .3px; }
  .association {
    position: absolute; top: 467px; left: 0; width: 100%;
    font-weight: 700; font-size: 15px; color: var(--magenta);
  }
  .presents {
    position: absolute; top: 492px; left: 0; width: 100%;
    font-weight: 300; font-size: 22px; letter-spacing: .5px; color: var(--ink);
  }
  .title {
    position: absolute; top: 519px; left: 0; width: 100%;
    font-weight: 800; font-size: 64px; line-height: 67px; color: var(--magenta); letter-spacing: .5px;
  }
  .cast-band {
    position: absolute; top: 654px; left: 0; width: 584px; height: 74px; background: var(--magenta);
    color: #fff; font-weight: 600; font-size: 15.5px; line-height: 22px; padding-top: 15px; letter-spacing: .2px;
  }
  .cast-band .sep { margin: 0 12px; font-weight: 300; }
  .credits {
    position: absolute; top: 741px; left: 0; width: 100%; font-family: "Cinzel", serif; color: var(--ink);
  }
  .credit { position: absolute; width: 180px; text-align: center; }
  .credit .role { display: block; font-size: 6.5px; letter-spacing: .4px; line-height: 9px; }
  .credit .name { display: block; font-size: 13.5px; line-height: 16px; letter-spacing: .4px; }
  .credit--editor { left: 29px; top: 0; }
  .credit--costume { left: 205px; top: 0; }
  .credit--score { left: 380px; top: 0; }
  .credit--photo { left: 142px; top: 34px; width: 300px; }
  .base-rule { position: absolute; left: 0; top: 808px; width: 584px; height: 10px; background: var(--magenta); }
</style>
</head>
<body>
<div class="stage">
  <article class="poster">
    <div class="key-photo" role="img" aria-label="Photo of a smiling couple standing together outdoors under trees"></div>
    <div class="accent-band"></div>
    <figure class="still still--night"><span role="img" aria-label="Film still of the couple in a dim evening setting"></span></figure>
    <figure class="still still--sepia"><span role="img" aria-label="Sepia film still of the young couple sitting outdoors"></span></figure>
    <figure class="still still--cafe"><span role="img" aria-label="Film still of two people talking at a restaurant counter"></span></figure>

    <p class="studios">MARROW LANE FILMS <small>AND</small> BRIGHT ORCHARD PRODUCTIONS</p>
    <p class="association"><small>IN ASSOCIATION WITH</small> KESTREL MEDIA</p>
    <p class="presents">PRESENTS</p>
    <h1 class="title">PAINTED<br>LANTERNS</h1>

    <div class="cast-band">
      <p>CLARA BENTON<span class="sep">|</span>JULIAN MARSH<span class="sep">|</span>DESMOND HALLOWAY</p>
      <p>OWEN FAIRBANKS<span class="sep">|</span>LEO VARGA<span class="sep">|</span>NINA CASTELL</p>
    </div>

    <div class="credits">
      <p class="credit credit--editor"><span class="role">EDITED BY</span><span class="name">EVAN ROWLEY</span></p>
      <p class="credit credit--costume"><span class="role">COSTUME DESIGNER</span><span class="name">DIANE KOWAL</span></p>
      <p class="credit credit--score"><span class="role">ORIGINAL SCORE BY</span><span class="name">MILES GRANT</span></p>
      <p class="credit credit--photo"><span class="role">DIRECTORS OF PHOTOGRAPHY</span><span class="name">PETER LINDQVIST MARK HENLEY</span></p>
    </div>
    <div class="base-rule"></div>
  </article>
</div>
</body>
</html>
```